Bluvora business website

I am wanting a website for my media agency Bluvora.

It needs to be be an attractive, unique and professional looking website. The website is a destination for people to be able to understand the service that Bluvora offers.

Please read uploaded website copy to gain an understanding of the business.

Target Market(s)

small business owners, business decision makers, marketing managers,

Industry/Entity Type

Business

Requirements
Must have
• Good branding.

```html
<!DOCTYPE html>
<html lang="en">
<head>
<meta charset="utf-8">
<title>Bluvora – Media Strategy, Planning and Trading</title>
<link rel="stylesheet" href="https://fonts.googleapis.com/css2?family=Open+Sans:wght@400;600&family=Arimo:wght@400;700&family=Cormorant+Garamond:ital,wght@1,500&family=Oswald:wght@600&display=swap">
<style>
  :root {
    --black: #000000;
    --charcoal: #2b2b2b;
    --footer: #3a3a3a;
    --white: #ffffff;
    --royal: #1f3ff0;
    --nav-active: #2fa4f0;
    --nav: #d8d8d8;
    --sky: #2a9fe0;
    --swatch-1: #2340d8;
    --swatch-2: #5459d6;
    --swatch-3: #bbbbbb;
    --brand-blue: #1010e0;
    --brand-violet: #5a4fe6;
  }
  * { box-sizing: border-box; margin: 0; padding: 0; }
  html, body { width: 1200px; height: 921px; overflow: hidden; background: var(--black); }
  .page { position: relative; width: 1200px; height: 921px; overflow: hidden; font-family: "Arimo", Arial, sans-serif; }

  /* Header */
  .site-header { position: absolute; left: 0; top: 0; width: 1200px; height: 99px; background: var(--black); }
  .brand { position: absolute; left: 137px; top: 3px; display: flex; align-items: center; gap: 20px; }
  .brand-dot { width: 56px; height: 56px; border-radius: 50%; background: var(--royal); }
  .brand-name { font-family: "Open Sans", sans-serif; font-size: 34px; font-weight: 400; color: var(--white); letter-spacing: 1px; }
  .header-disc { position: absolute; left: 530px; top: -92px; width: 134px; height: 134px; border-radius: 50%; background: #333; }
  .social { position: absolute; left: 982px; top: 4px; display: flex; gap: 8px; }
  .social span { width: 18px; height: 18px; border-radius: 50%; background: var(--white); display: block; }
  .main-nav { position: absolute; top: 54px; left: 562px; display: flex; gap: 30px; font-family: "Open Sans", sans-serif; font-size: 14px; }
  .main-nav a { color: var(--nav); text-decoration: none; }
  .main-nav a.is-active { color: var(--nav-active); }

  /* Hero */
  .hero-backdrop { position: absolute; left: 0; top: 99px; width: 1200px; height: 623px;
    background:
      linear-gradient(125deg, rgba(255,240,80,.75) 0%, rgba(255,160,220,.55) 22%, rgba(255,255,255,.4) 40%, rgba(150,230,255,.6) 62%, rgba(40,210,240,.8) 100%),
      linear-gradient(200deg, #ffb0e6 0%, #ffffff 45%, #7fe4f5 100%); }
  .hero-shadow { position: absolute; left: 40px; top: 680px; width: 1010px; height: 36px; border-radius: 50%;
    background: radial-gradient(ellipse at center, rgba(0,0,0,.85) 0%, rgba(0,0,0,.4) 55%, rgba(0,0,0,0) 75%); }
  .slide { position: absolute; left: 24px; top: 138px; width: 1043px; height: 540px; background: var(--white); overflow: hidden; }
  .slide-panel { position: absolute; left: 0; top: 0; }
  .slide-copy { position: absolute; left: 112px; top: 188px; width: 340px; color: var(--white); font-size: 13px; line-height: 15.5px; text-indent: 12px; }
  .swatches { position: absolute; top: 405px; left: 132px; }
  .swatch { position: absolute; top: 0; width: 57px; height: 57px; border-radius: 4px; border: 1px solid #111; box-shadow: 1px 2px 3px rgba(0,0,0,.6); }
  .swatch--one { left: 0; background: var(--swatch-1); }
  .swatch--two { left: 107px; background: var(--swatch-2); }
  .swatch--three { left: 210px; background: var(--swatch-3); }
  .slide-brand { position: absolute; left: 560px; top: 200px; display: flex; align-items: center; gap: 22px; }
  .slide-brand-square { width: 70px; height: 70px; background: var(--brand-violet); }
  .slide-brand-name { font-family: "Arimo", Arial, sans-serif; font-weight: 700; font-size: 92px; color: var(--brand-blue); }

  /* Footer */
  .site-footer { position: absolute; left: 0; top: 722px; width: 1200px; height: 199px;
    background: linear-gradient(100deg, #3b3b3b 0%, #3f3a44 35%, #3a3a3a 60%, #2e4a52 85%, #3a3a3a 100%); }
  .footer-heading { position: absolute; top: 28px; font-family: "Cormorant Garamond", serif; font-style: italic; font-weight: 500; font-size: 31px; color: var(--sky); }
  .footer-heading--specialties { left: 146px; }
  .footer-heading--industry { left: 457px; }
  .footer-heading--contacts { left: 784px; top: 35px; font-family: "Oswald", sans-serif; font-style: normal; font-weight: 600; font-size: 22px; letter-spacing: .3px; }
  .footer-rule { position: absolute; left: 118px; width: 935px; height: 6px; border-radius: 50%;
    background: radial-gradient(ellipse at center, rgba(255,255,255,.55) 0%, rgba(255,255,255,.15) 60%, rgba(255,255,255,0) 80%); }
  .footer-rule--top { top: 83px; }
  .footer-rule--bottom { top: 161px; }
  .footer-text { position: absolute; top: 104px; color: var(--white); font-size: 11.5px; line-height: 15px; }
  .footer-text--specialties { left: 137px; width: 270px; }
  .footer-text--industry { left: 448px; }
  .footer-text--contacts { left: 770px; top: 99px; font-size: 11px; line-height: 14.5px; }
</style>
</head>
<body>
<div class="page">
  <header class="site-header">
    <div class="brand">
      <span class="brand-dot"></span>
      <span class="brand-name">Bluvora</span>
    </div>
    <div class="header-disc"></div>
    <div class="social" aria-label="Social links">
      <span></span><span></span><span></span>
    </div>
    <nav class="main-nav">
      <a class="is-active" href="#">HOME</a>
      <a href="#">About</a>
      <a href="#">What we do</a>
      <a href="#">People</a>
      <a href="#">Ideas</a>
      <a href="#">Contact us</a>
    </nav>
  </header>

  <div class="hero-backdrop" role="img" aria-label="Colourful abstract backdrop of overlapping translucent triangles in yellow, pink and cyan"></div>
  <div class="hero-shadow"></div>

  <section class="slide">
    <svg class="slide-panel" width="1043" height="540" viewBox="0 0 1043 540" aria-hidden="true">
      <polygon points="0,0 431,0 519,540 0,540" fill="#2b2b2b"/>
    </svg>
    <p class="slide-copy">Bluvora is a media strategy, planning and trading agency that specialises in implementing creative content led strategy with our media partners enabling businesses to achieve higher levels of brand exposure in the media landscape resulting in increased return on their media investment</p>
    <div class="swatches">
      <span class="swatch swatch--one"></span>
      <span class="swatch swatch--two"></span>
      <span class="swatch swatch--three"></span>
    </div>
    <div class="slide-brand">
      <span class="slide-brand-square"></span>
      <span class="slide-brand-name">Bluvora</span>
    </div>
  </section>

  <footer class="site-footer">
    <h2 class="footer-heading footer-heading--specialties">Specialties</h2>
    <h2 class="footer-heading footer-heading--industry">Industry</h2>
    <h2 class="footer-heading footer-heading--contacts">CONTACTS</h2>
    <div class="footer-rule footer-rule--top"></div>
    <p class="footer-text footer-text--specialties">Media Strategy, Media Planning, Media Trading, Content and Integration</p>
    <p class="footer-text footer-text--industry">Marketing and Advertising</p>
    <p class="footer-text footer-text--contacts">mara.lind@bluvora.com.au<br>(02) 5550 1234<br>PO Box 000 000 Harbourview Australia</p>
    <div class="footer-rule footer-rule--bottom"></div>
  </footer>
</div>
</body>
</html>
```